依頼詳細
残暑お見舞い申し上げます

コロナ禍と暑さで汗が噴き出るような日々が続きますが、いかがお過ごしでしょうか?
汗はかけばかくほど、老廃物が体内から出て、心も体も健康になります。
汗をかかないようにすることは、決して良いことではありません。
会社にとっても、今年は汗(特別損失)を出せるチャンスです。
個人も会社もたくさんの汗を出して、より健康体になられること、心より祈念申し上げます。

★写真に添える文章:松本清志の最新刊
「伸びる会社へ組み直す」
定価10,780円(税込み)
記載項目
ノルフェン・パートナーズ
松本 清志・長谷 宗一郎・柴田 昌平
希望イメージ
シンプル 複雑
単色 カラフル
暗い 明るい
日常 高級
遊び心 厳粛
未来的 伝統的
女性的 男性的
希望する色
水色系
納品ファイル
• 高解像度JPG (.jpg)
補足説明
■ 選んだ理由

今年はコロナのイベント中止で花火大会もなくなるなかで、
もってこいのデザインでした。
文字の並べ方に工夫が見られ、メッセージとバックのコントラストが素敵でした。
一目見ておしゃれで気に入りました。

■ 提案者全員のお礼・コメント

この度は、ご応募ありがとうございました。
毎回、新たなご提案が来るのが楽しみでした。素敵なご応募をありがとうございました。

```html
<!DOCTYPE html>
<html lang="ja">
<head>
<meta charset="utf-8">
<title>残暑お見舞い</title>
<link rel="stylesheet" href="https://fonts.googleapis.com/css2?family=Noto+Sans+JP:wght@500;700&family=Shippori+Mincho:wght@600;700&display=swap">
<style>
  :root {
    --sky-top: #e9f6fd;
    --sky-mid: #3d8fd8;
    --sea-deep: #0b3f8f;
    --sea-dark: #06306f;
    --ink-light: #ffffff;
    --ink-title: #1a4b8c;
    --book-red: #8e1a1a;
    --book-dark: #2a0c0c;
  }
  html, body {
    margin: 0;
    padding: 0;
    width: 825px;
    height: 1200px;
    overflow: hidden;
  }
  .card {
    position: relative;
    width: 825px;
    height: 1200px;
    overflow: hidden;
    background:
      radial-gradient(ellipse 520px 300px at 50% 0%, rgba(255,255,255,0.95), rgba(255,255,255,0) 70%),
      radial-gradient(ellipse 360px 260px at 12% 100%, rgba(140,210,255,0.55), rgba(140,210,255,0) 70%),
      linear-gradient(180deg, var(--sky-top) 0%, #a9d6f4 12%, var(--sky-mid) 30%, var(--sea-deep) 62%, var(--sea-dark) 100%);
    font-family: "Noto Sans JP", sans-serif;
  }
  .greeting-title {
    position: absolute;
    top: 82px;
    left: 0;
    width: 100%;
    margin: 0;
    text-align: center;
    font-family: "Noto Sans JP", sans-serif;
    font-weight: 500;
    font-size: 42px;
    line-height: 56px;
    letter-spacing: 2px;
    color: var(--ink-title);
  }
  .message {
    position: absolute;
    top: 200px;
    left: 150px;
    width: 600px;
    margin: 0;
    color: var(--ink-light);
    font-weight: 700;
    font-size: 23px;
    line-height: 42px;
    text-shadow: 0 1px 3px rgba(0,30,80,0.35);
  }
  .message p { margin: 0; white-space: nowrap; }
  .sender {
    position: absolute;
    top: 650px;
    left: 344px;
    width: 430px;
    color: var(--ink-light);
    font-weight: 500;
    font-size: 21px;
    line-height: 42px;
    white-space: nowrap;
  }
  .sender p { margin: 0; }
  .sender .company { margin-left: 63px; }
  .book-visual {
    position: absolute;
    left: 503px;
    top: 784px;
    width: 197px;
    height: 386px;
    border-radius: 3px;
    background: linear-gradient(160deg, #c2302a 0%, var(--book-red) 45%, var(--book-dark) 100%);
    box-shadow: 12px 16px 26px rgba(0,10,40,0.5);
  }
  .book-caption {
    position: absolute;
    left: 170px;
    top: 952px;
    margin: 0;
    color: var(--ink-light);
    font-family: "Shippori Mincho", serif;
    font-weight: 600;
    font-size: 19px;
    line-height: 27px;
  }
</style>
</head>
<body>
  <main class="card">
    <h1 class="greeting-title">残暑お見舞い申し上げます</h1>

    <div class="message">
      <p>コロナ禍と暑さで汗が噴き出るような日々が続きます</p>
      <p>が、いかがお過ごしでしょうか?</p>
      <p>汗はかけばかくほど、老廃物が体内から出て、心も</p>
      <p>体も健康になります。</p>
      <p>汗をかかないようにすることは、決して良いことでは</p>
      <p>ありません。</p>
      <p>会社にとっても、今年は汗(特別損失)を出せる</p>
      <p>チャンスです。</p>
      <p>個人も会社もたくさんの汗を出して、より健康体に</p>
      <p>なられること、心より祈念申し上げます。</p>
    </div>

    <div class="sender">
      <p class="company">ノルフェン・パートナーズ</p>
      <p class="people">松本 清志・長谷 宗一郎・柴田 昌平</p>
    </div>

    <div class="book-visual" role="img" aria-label="新刊書籍「伸びる会社へ組み直す」の表紙写真"></div>

    <p class="book-caption">松本清志の最新刊<br>「伸びる会社へ組み直す」<br>定価 10,780円(税込み)</p>
  </main>
</body>
</html>
```